Refresh of The Marston Collective business card

Update business card design using existing primary logo. Names, numbers, etc. are too hard to read on current design.

Target Market(s)

We are a CPA firm.

Industry/Entity Type

Accountant

Contact Information for Business Card

update current card

Colors
0355a3
3176b5
85acd3
0792cd

Requirements
Must have
• Easier to read phone numbers and names
• Use existing logo
Nice to have
• We love our color scheme and current TMC logo. But the names and phone numbers are too small and card just look old and stale.

```html
<!DOCTYPE html>
<html lang="en">
<head>
<meta charset="utf-8">
<title>The Marston Collective – Business Card</title>
<link rel="stylesheet" href="https://fonts.googleapis.com/css2?family=Tinos&family=Questrial&family=Montserrat:wght@500&display=swap">
<style>
  :root {
    --page: #ffffff;
    --card-core: #1a62ad;
    --card-mid: #173f72;
    --card-edge: #0e1829;
    --ink: #ffffff;
    --ink-soft: #dfe8f3;
    --navy: #17335e;
  }
  * { box-sizing: border-box; margin: 0; padding: 0; }
  html, body { width: 1200px; height: 927px; overflow: hidden; background: var(--page); }
  .sheet { position: relative; width: 1200px; height: 927px; }
  .card {
    position: absolute; left: 277px; width: 646px; height: 368px;
    border-radius: 18px; overflow: hidden;
    background: radial-gradient(ellipse 62% 68% at 50% 52%, var(--card-core) 0%, var(--card-mid) 55%, var(--card-edge) 100%);
    color: var(--ink);
  }
  .card--front { top: 54px; }
  .card--back { top: 496px; }
  .brand { position: absolute; display: flex; align-items: center; }
  .brand__disc {
    width: 102px; height: 102px; border-radius: 50%;
    background: var(--ink); flex: none;
  }
  .brand__words { margin-left: 22px; }
  .brand__name {
    font-family: "Tinos", serif; font-size: 25px; line-height: 1.05;
    text-transform: uppercase; letter-spacing: 0.5px; color: var(--ink);
  }
  .brand__tagline {
    margin-top: 8px; font-family: "Montserrat", sans-serif; font-weight: 500;
    font-size: 8px; letter-spacing: 2.6px; text-transform: uppercase; color: var(--ink);
  }
  .card--front .brand { left: 161px; top: 37px; }
  .card--back .brand { left: 166px; top: 125px; }
  .holder {
    position: absolute; left: 40px; top: 268px;
    font-family: "Tinos", serif; font-size: 16.5px; letter-spacing: 0.3px;
  }
  .address {
    position: absolute; left: 40px; top: 303px;
    font-family: "Tinos", serif; font-size: 16px; line-height: 16px;
  }
  .contacts {
    position: absolute; right: 62px; top: 264px; list-style: none;
    font-family: "Tinos", serif; font-size: 15.5px; line-height: 16px; text-align: right;
  }
  .contacts li { display: flex; justify-content: flex-end; align-items: center; }
  .contacts svg { width: 11px; height: 11px; margin-left: 12px; flex: none; }
  .web {
    position: absolute; left: 0; right: 0; top: 266px; text-align: center;
    font-family: "Questrial", sans-serif; font-size: 17px; letter-spacing: 0.4px; color: var(--ink-soft);
  }
</style>
</head>
<body>
<main class="sheet">
  <section class="card card--front" aria-label="Card front">
    <div class="brand">
      <span class="brand__disc"></span>
      <div class="brand__words">
        <p class="brand__name">The Marston<br>Collective</p>
        <p class="brand__tagline">Certified Public Accountants</p>
      </div>
    </div>
    <p class="holder">DANIEL R. MARSTON, CPA</p>
    <p class="address">&nbsp;312 E. Larkspur Ave. Suite 104<br>Winter Park, Florida 32789</p>
    <ul class="contacts">
      <li>555.210.4836
        <svg viewBox="0 0 12 12" aria-label="office"><circle cx="6" cy="6" r="6" fill="#fff"/><path d="M3.8 3.2l1.2-.2.6 1.5-.8.6a4 4 0 0 0 2 2l.6-.8 1.5.6-.2 1.2C6 8.6 3.4 6 3.8 3.2z" fill="#17335e"/></svg></li>
      <li>555.347.9120
        <svg viewBox="0 0 12 12" aria-label="mobile"><circle cx="6" cy="6" r="6" fill="#fff"/><rect x="4.3" y="2.8" width="3.4" height="6.4" rx=".6" fill="#17335e"/></svg></li>
      <li>555.682.1574
        <svg viewBox="0 0 12 12" aria-label="fax"><circle cx="6" cy="6" r="6" fill="#fff"/><rect x="3.4" y="3.6" width="5.2" height="4.8" rx=".5" fill="#17335e"/></svg></li>
      <li>dan@themarstoncollective.com
        <svg viewBox="0 0 12 12" aria-label="email"><circle cx="6" cy="6" r="6" fill="#fff"/><rect x="3" y="4.4" width="6" height="3.4" fill="#17335e"/></svg></li>
    </ul>
  </section>

  <section class="card card--back" aria-label="Card back">
    <div class="brand">
      <span class="brand__disc"></span>
      <div class="brand__words">
        <p class="brand__name">The Marston<br>Collective</p>
        <p class="brand__tagline">Certified Public Accountants</p>
      </div>
    </div>
    <p class="web">www.themarstoncollective.com</p>
  </section>
</main>
</body>
</html>
```